Business Card Design Project

for a second hand vintage clothing store. shop name is The Velvet Loft

Cards to be double sided

The name on the card is Marianne Trelford

Information to put on card:

The Velvet Loft
Marianne Trelford (no job title)
84/227 Quayle St, Pyrmont, Sydney, NSW, 2009.
Mobile: 0412 975 206
Email: thevelvetloft@mailbox-example.com.au
Web: www.thevelvetloft-example.com.au

Target Market(s)

Women looking at vintage clothing

Industry/Entity Type

Clothing

```html
<!DOCTYPE html>
<html lang="en">
<head>
<meta charset="utf-8">
<title>The Velvet Loft – Business Card</title>
<link rel="stylesheet" href="https://fonts.googleapis.com/css2?family=Lora:wght@400;700&family=Noto+Sans:wght@700&display=swap">
<style>
  :root {
    --backdrop: #efe6cc;
    --maroon: #652a3b;
    --maroon-deep: #5a1e2e;
    --red-glow: #a3202c;
    --gold: #e6d49a;
    --gold-band: #ead8a2;
    --logo-gold: #d9c27e;
    --paper: #ffffff;
    --ink: #3a2a2e;
  }
  html, body {
    margin: 0;
    width: 1200px;
    height: 951px;
    overflow: hidden;
    background: var(--backdrop);
  }
  .canvas {
    position: relative;
    width: 1200px;
    height: 951px;
  }
  .card {
    position: absolute;
    width: 700px;
    height: 400px;
    border-radius: 24px;
    overflow: hidden;
    box-shadow: 0 6px 18px rgba(80, 50, 30, 0.18);
  }
  .card--front {
    left: 130px;
    top: 40px;
    background: var(--maroon);
    display: flex;
    align-items: center;
    justify-content: center;
  }
  .brand {
    font-family: "Lora", serif;
    font-weight: 400;
    color: var(--logo-gold);
    margin: 0;
  }
  .card--front .brand { font-size: 76px; }
  .card--back {
    left: 370px;
    top: 500px;
    background: var(--paper);
  }
  .card-shapes {
    position: absolute;
    inset: 0;
  }
  .card--back .brand {
    position: absolute;
    left: 40px;
    top: 50px;
    font-size: 42px;
  }
  .contact {
    position: absolute;
    left: 40px;
    top: 200px;
    margin: 0;
    padding: 0;
    list-style: none;
    font-family: "Noto Sans", sans-serif;
    font-weight: 700;
    font-size: 17px;
    line-height: 1.3;
    color: var(--ink);
  }
  .contact li {
    display: flex;
    align-items: flex-start;
    gap: 10px;
    margin-bottom: 8px;
  }
  .contact svg {
    flex: none;
    width: 16px;
    height: 16px;
    margin-top: 3px;
    fill: var(--maroon);
  }
  .contact .email { font-size: 14.5px; }
  .contact .web { font-size: 15.5px; }
  .holder-name {
    position: absolute;
    left: 480px;
    top: 150px;
    width: 200px;
    margin: 0;
    text-align: center;
    font-family: "Lora", serif;
    font-weight: 700;
    font-size: 30px;
    line-height: 1.25;
    color: var(--paper);
  }
</style>
</head>
<body>
<main class="canvas">

  <section class="card card--front" aria-label="Card front">
    <h1 class="brand">The Velvet Loft</h1>
  </section>

  <section class="card card--back" aria-label="Card back">
    <svg class="card-shapes" viewBox="0 0 700 400" aria-hidden="true">
      <defs>
        <radialGradient id="panelGlow" cx="0.45" cy="0.5" r="0.7">
          <stop offset="0" stop-color="#a3202c"/>
          <stop offset="1" stop-color="#5a1e2e"/>
        </radialGradient>
      </defs>
      <path d="M388,0 C462,110 470,270 392,400 L430,400 C505,270 498,120 430,0 Z" fill="#ead8a2"/>
      <path d="M372,0 C420,50 440,120 440,210 C430,120 410,55 350,0 Z" fill="#5a1e2e"/>
      <path d="M430,0 C500,120 505,270 430,400 L700,400 L700,0 Z" fill="url(#panelGlow)"/>
    </svg>

    <h2 class="brand">The Velvet Loft</h2>

    <ul class="contact">
      <li>
        <svg viewBox="0 0 16 16"><path d="M8 1 L15 8 H13 V15 H10 V10 H6 V15 H3 V8 H1 Z"/></svg>
        <span>84/227 Quayle St, Pyrmont,<br>Sydney, NSW, 2009.</span>
      </li>
      <li>
        <svg viewBox="0 0 16 16"><rect x="4" y="1" width="8" height="14" rx="2"/></svg>
        <span>0412 975 206</span>
      </li>
      <li>
        <svg viewBox="0 0 16 16"><path d="M1 4 H15 V13 H1 Z M1 4 L8 9 L15 4" stroke="#fff" stroke-width="1"/></svg>
        <span class="email">thevelvetloft@mailbox-example.com.au</span>
      </li>
      <li>
        <svg viewBox="0 0 16 16"><circle cx="8" cy="8" r="7"/></svg>
        <span class="web">www.thevelvetloft-example.com.au</span>
      </li>
    </ul>

    <p class="holder-name">Marianne<br>Trelford</p>
  </section>

</main>
</body>
</html>
```